Brochure Design Project - KelvoraPartners.com.au

Hi,

I am establishing a new business in professional services for "www.KelvoraPartners.com.au".

The website is currently getting developed, so in the interim I would like a e-brochure to send out to my clients.

I have attached a draft layout/content for the brochure.

Please use the same content, in the same order - but i would like some creative in put on the remainder.

Target Market(s)

Financial Advisers, Accountants, Lawyers

Industry/Entity Type

Business

Requirements
Must have
• - must be modern and engaging to look at.
- attached is the colour scheme for the website. Please limit the colours/fonts/format to match the brand of KelvoraPartners.com.au

- on the home page I need to have space for imbedding two youtube video's. The video's will be completed within a week, so I can provide the links then.

- if you do know know how to imbed video's into a PDF brochure, please leave it out.

```html
<!DOCTYPE html>
<html lang="en">
<head>
<meta charset="utf-8">
<title>KelvoraPartners.com.au – Brochure</title>
<link href="https://fonts.googleapis.com/css2?family=Arimo:wght@400;700&display=swap" rel="stylesheet">
<style>
:root{
  --peach:#fde3c8;
  --peach-soft:#fdeadb;
  --band-edge:#c9a27c;
  --orange:#f5a33a;
  --brown:#8a4513;
  --text:#454545;
  --white:#ffffff;
}
*{margin:0;padding:0;box-sizing:border-box}
html,body{width:1200px;height:900px;overflow:hidden;background:var(--white)}
body{position:relative;font-family:"Arimo",Arial,sans-serif;color:var(--text);font-size:11.4px;line-height:16px}
.top-band{position:absolute;left:0;top:0;width:1200px;height:101px;background:var(--peach)}
.top-band::after{content:"";position:absolute;left:0;top:101px;width:100%;height:8px;background:linear-gradient(var(--band-edge),rgba(201,162,124,0))}
.brand{position:absolute;top:40px;display:flex;align-items:center;gap:8px}
.brand-mark{width:92px;height:44px;background:var(--orange);border-radius:6px}
.brand-name{font-weight:700;font-size:18px;line-height:20px;color:var(--brown);letter-spacing:-.3px}
.brand-tag{font-size:8.5px;line-height:10px;color:var(--text)}
.brand-left{left:40px}.brand-right{left:640px}
.hero-photo{position:absolute;left:0;top:115px;width:265px;height:785px;
  background:linear-gradient(180deg,#9cc9ef 0%,#5b98dc 35%,#2d66b8 65%,#1c3f7c 100%)}
.lower-right{position:absolute;left:600px;top:528px;width:600px;height:372px;background:var(--peach-soft)}
.chart-art{position:absolute;left:395px;top:605px;width:185px;height:295px;
  background:linear-gradient(180deg,rgba(251,230,210,0) 0%,#fbe6d2 45%,#fbe6d2 100%)}
.section-title{position:absolute;font-weight:700;font-size:18.5px;line-height:22px;color:var(--brown)}
.col{position:absolute}
.col p{margin-bottom:6px}
.col h3{font-size:13px;line-height:16px;font-weight:700;color:var(--brown);margin-bottom:6px}
.col ul{list-style:none;margin-bottom:2px}
.col li{padding-left:15px;position:relative;margin-bottom:3px}
.col li::before{content:"•";position:absolute;left:2px;color:var(--orange)}
</style>
</head>
<body>
<header class="top-band">
  <div class="brand brand-left">
    <div class="brand-mark"></div>
    <div><div class="brand-name">KelvoraPartners.com.au</div><div class="brand-tag">Get Quotes &amp; Contact Professional Advisers.</div></div>
  </div>
  <div class="brand brand-right">
    <div class="brand-mark"></div>
    <div><div class="brand-name">KelvoraPartners.com.au</div><div class="brand-tag">Get Quotes &amp; Contact Professional Advisers.</div></div>
  </div>
</header>

<div class="hero-photo" role="img" aria-label="Businessman in a suit, seen from behind, facing a blue stock market board"></div>
<div class="lower-right"></div>
<div class="chart-art" role="img" aria-label="Faint rising arrow over a growing bar chart"></div>

<svg style="position:absolute;left:280px;top:150px" width="245" height="70" viewBox="0 0 245 70" aria-hidden="true">
  <path d="M40 6 H242 L222 64 H40 Z" fill="var(--orange)"/>
  <path d="M46 11 H233 L217 59 H46 Z" fill="var(--white)"/>
  <circle cx="34" cy="35" r="33" fill="var(--orange)"/>
  <circle cx="34" cy="35" r="26" fill="var(--white)"/>
  <path d="M25 22c3-2 5 0 6 3l1 4c0 2-2 3-3 4 1 4 3 7 6 9 1-1 2-3 4-3l4 1c3 1 5 3 3 6l-2 2c-10 1-21-11-21-22z" fill="#555"/>
</svg>
<div class="section-title" style="left:360px;top:174px">Services</div>

<svg style="position:absolute;left:634px;top:150px" width="325" height="70" viewBox="0 0 325 70" aria-hidden="true">
  <path d="M40 6 H322 L302 64 H40 Z" fill="var(--orange)"/>
  <path d="M46 11 H313 L297 59 H46 Z" fill="var(--white)"/>
  <circle cx="34" cy="35" r="33" fill="var(--orange)"/>
  <circle cx="34" cy="35" r="26" fill="var(--white)"/>
  <circle cx="28" cy="29" r="6" fill="#555"/><path d="M17 47c0-8 5-11 11-11s11 3 11 11z" fill="#555"/>
  <circle cx="41" cy="27" r="5.5" fill="#777"/><path d="M35 34c2-1 4-1 6-1 6 0 10 3 10 10h-9c0-4-2-7-7-9z" fill="#777"/>
</svg>
<div class="section-title" style="left:715px;top:174px">Client Matching Service</div>

<section class="col" style="left:285px;top:235px;width:280px">
  <p>Adviser Profile &amp; Directory Listing</p>
  <p>All subscribed advisers have the ability to create a unique ‘Adviser Profile’ that can be tailored to themselves and their firm.</p>
  <p>Via an 8 part questionnaire, advisers can share information on all aspects of their advisory business on their ‘Adviser Profile’. They can also upload a color scheme, logo, profile picture, banner, video presentation and documents to brand their profile.</p>
  <p>There is no obligation to complete the entire questionnaire. Advisers are entitled to disclose as much information as they want on their ‘Adviser Profiles’.</p>
  <p>The ‘Adviser Profile’ will act like an online brochure and will be cataloged in the KelvoraPartners directory. Once it is listed in the directory, the ‘Adviser Profile’ is made public and can be easily found by any user via the ‘Search’ function.</p>
</section>

<section class="col" style="left:636px;top:235px;width:254px">
  <p>The Client Matching Service is based on a highly sophisticated algorithm and is the backbone of KelvoraPartners. It ensures that advisers are provided with leads from clients that actually want their advice!</p>
  <p>When a clients wants to be contacted with quotes from advisers, they can submit an ‘Advice Request’ through the system.</p>
  <p>The ‘Advice Request’ is a two-minute form, which allows the client to share details on the type of adviser they want, a brief description of their professional problem and a budget for the work.</p>
  <p>KelvoraPartners uses the information on the ‘Advice Request’ and compares it to data on all the ‘Adviser Profiles’ on the system to find the top 5 advisers.</p>
</section>

<section class="col" style="left:906px;top:235px;width:260px">
  <p>If more than 5 advisers meet the same criteria, the system will then find the top 5 advisers based on their recommendations.</p>
  <p>The matched advisers will be immediately notified via email. They will have 2 business days to review the ‘Advice Request’ and contact the client. If the adviser fails to contact the client, the next suitable adviser is notified.</p>
  <p>The contact details of the client will remain anonymous. If the adviser is able assist the client upon reviewing the ‘Advice Request’, they can click the ‘Contact’ button and the contact details will be made available.</p>
  <p>The Key Differentiator between KelvoraPartners is that the adviser has the ability to self assess their leads and there is no obligation to proceed.</p>
</section>

<section class="col" style="left:636px;top:538px;width:254px">
  <h3>Blog</h3>
  <p>KelvoraPartners has also been developed to serve as a central education centre for clients. We want clients to use KelvoraPartners as the first place to ask questions and retrieve invaluable information about the related industries.</p>
  <p>We have therefore opened up our ‘Blog’ to allow advisers to publish information such as ‘market commentaries’, journals, presentations, video’s and so forth. The aim is for advisers to gain indirect marketing whilst also educating the broader community.</p>
  <p>In order to monitor the ‘Blog’, all content will be published by KelvoraPartners on behalf of the adviser. This ensures that all content is relevant, engaging and allows for fair representation of all advisers.</p>
</section>

<section class="col" style="left:906px;top:538px;width:260px">
  <h3>Home Page Feature</h3>
  <p>In order to build a stronger online presence, KelvoraPartners is offering up to 4 ‘Blog’ postigs and up to 5 advisers to be featured on the KelvoraPartners home page.</p>
  <p>You profile will be immediately available to all users who visit the KelvoraPartners homepage which will drive additional traffic to your profile and your credibility.</p>
  <h3 style="margin-top:12px">Comprehensive Statistics</h3>
  <p>KelvoraPartners also allows advisers to track all activity on their account and ‘Adviser Profile’.</p>
  <ul>
    <li>Number of visitors</li>
    <li>Number of appearances in Search</li>
    <li>Number of matched clients</li>
    <li>Number of contacted clients</li>
  </ul>
  <p>KelvoraPartners will provide information on how to improve the performance of your profile.</p>
</section>
</body>
</html>
```